Lumivane, Business Intelligence Consultant Web Design

We need a web design for a Business Intelligence Consultant Enterprise.
We design, develop and mantain management systems and reports that delivered to the final user a complete information about their business. With that information they can take better management decisions.
Our principal service is KRV Business Intelligence proyects, using KRV Stockvault and KRV Quillmark tools.
Also we develop web systems that integrate mobile technology with KRV Systems and end user database systems.

Our principal objective is to be a partner of our clients more than a service provider, the idea is to offer a complete service to our customers that allow both companies grow togheter.

The final design must present our list of services and products, and show our experience in business intelligence projects.

Target Market(s)

Companies that runs KRV systems, Business companies, companies with production processes, retail, logistic process (inventory management)

Industry/Entity Type

Business

Requirements
Must have
• The brochure must have 4 pages:
Home
Empresa
Business Intelligence
Aplicaciones empresariales móviles
Metodología

And a contact form to receive customer contact.
- Name
- Company
- Contact Email
- Message text

For the color I will upload both company logos with different colors that u can use. Obviously you can add color if you want.
Nice to have
• The principal idea is to show to customer that all information of his business can be summarized on one graphic panel and can be consulted from any device.

Is nice to have business graphics on the web design, maybe abstract and give the idea of management information can be obtained easily.

Should not have
• Please, PLEASE!, don't use on the web site a meeting photo or people watching a business report on a lobby or some business man making a presentation.
Neither images of team building or people at the office.

That images are too used to present the business intelligence concept and the principal idea is to have information, and not people working hard to obtain that.

```html
<!DOCTYPE html>
<html lang="es">
<head>
<meta charset="utf-8">
<title>Lumivane – Business Intelligence</title>
<link href="https://fonts.googleapis.com/css2?family=Arimo:wght@400;700&family=Ubuntu:wght@300;400&display=swap" rel="stylesheet">
<style>
  :root {
    --red: #d9121f;
    --accent: #ef5a3c;
    --dark: #333333;
    --panel: #f7f7f7;
    --rule: #dddddd;
    --text: #1a1a1a;
    --grey: #8a8a8a;
    --white: #ffffff;
    --banner-a: #5e84a6;
    --banner-b: #8fb0cc;
  }
  * { box-sizing: border-box; margin: 0; padding: 0; }
  html, body { width: 1060px; height: 1200px; overflow: hidden; background: var(--white); }
  body { position: relative; font-family: "Arimo", Arial, sans-serif; color: var(--text); }

  .brand { position: absolute; left: 125px; top: 38px; display: flex; align-items: center; gap: 12px; }
  .brand-mark { width: 30px; height: 30px; background: var(--red); }
  .brand-name { font-family: "Ubuntu", sans-serif; font-weight: 400; font-size: 40px; color: var(--grey); line-height: 1; }

  .social { position: absolute; display: flex; align-items: center; gap: 4px; font-size: 11px; color: var(--text); }
  .social span.label { margin-right: 5px; }
  .social i { display: block; width: 16px; height: 16px; border-radius: 3px; background: #6b8bc4; }
  .social i:nth-of-type(2) { background: #45b0e0; }
  .social i:nth-of-type(3) { background: #2e7fb5; }
  .social i:nth-of-type(4) { background: #f0892e; }
  .social--top { left: 803px; top: 43px; }
  .social--bottom { left: 820px; top: 1156px; }

  .search { position: absolute; left: 737px; top: 76px; width: 199px; height: 23px; border-radius: 5px;
    background: linear-gradient(#3a3a3a, #111); color: var(--white); font-size: 12px; padding: 4px 13px; }
  .search svg { position: absolute; right: 9px; top: 5px; }

  .nav { position: absolute; left: 106px; top: 122px; width: 848px; height: 47px; background: var(--dark); }
  .nav a { position: absolute; top: 14px; transform: translateX(-50%); color: var(--white); font-weight: 700;
    font-size: 12.5px; text-decoration: none; white-space: nowrap; }
  .nav a.current { top: 11px; transform: none; left: 253px; width: 137px; text-align: center; background: var(--white);
    color: #111; border-radius: 4px; padding: 3px 0; }
  .nav .sep { position: absolute; top: 11px; width: 1px; height: 28px; background: #5a5a5a; }

  .banner { position: absolute; left: 0; top: 169px; width: 1060px; height: 167px;
    background: linear-gradient(90deg, var(--banner-a), var(--banner-b) 55%, var(--banner-a)); }

  .content { position: absolute; left: 106px; top: 336px; width: 848px; height: 635px; background: var(--panel);
    border-left: 1px solid var(--rule); border-right: 1px solid var(--rule); }
  .content h1 { position: absolute; left: 20px; top: 26px; font-size: 29px; font-weight: 700; color: var(--red); }
  .photo { position: absolute; left: 20px; top: 85px; width: 212px; height: 139px;
    background: linear-gradient(135deg, #c9ced4, #7d8690 60%, #3f4650); }
  .intro { position: absolute; left: 252px; top: 87px; width: 580px; }
  .content h2 { font-family: "Ubuntu", sans-serif; font-weight: 300; font-size: 21px; color: #333; margin-bottom: 6px; }
  .content p { font-size: 10.8px; line-height: 22px; }
  .body { position: absolute; left: 18px; top: 238px; width: 816px; }
  .body p + p { margin-top: 22px; }
  .body h2 { margin-top: 22px; margin-bottom: 4px; }

  .footer { position: absolute; left: 0; top: 971px; width: 1060px; height: 166px; background: var(--dark); color: var(--white); }
  .footer-inner { position: absolute; left: 131px; top: 28px; width: 800px; }
  .footer h3 { font-size: 10.5px; font-weight: 700; margin-bottom: 9px; }
  .footer h3 em { font-style: normal; color: var(--accent); }
  .footer p { font-size: 11.5px; line-height: 17.7px; margin-bottom: 4px; }

  .legal { position: absolute; left: 108px; top: 1159px; font-size: 10px; color: #333; }
</style>
</head>
<body>
  <header>
    <div class="brand"><span class="brand-mark"></span><span class="brand-name">Lumivane</span></div>
    <div class="social social--top"><span class="label">Follow Us</span><i></i><i></i><i></i><i></i></div>
    <div class="search">Search
      <svg width="14" height="14" viewBox="0 0 14 14"><circle cx="5.5" cy="5.5" r="4" fill="none" stroke="#aaa" stroke-width="1.6"/><line x1="8.5" y1="8.5" x2="13" y2="13" stroke="#aaa" stroke-width="2"/></svg>
    </div>
    <nav class="nav">
      <a href="#" style="left:80px">Home</a>
      <span class="sep" style="left:130px"></span>
      <a href="#" style="left:177px">Empresa</a>
      <span class="sep" style="left:232px"></span>
      <a href="#" class="current">Business Intelligence</a>
      <span class="sep" style="left:415px"></span>
      <a href="#" style="left:548px">Aplicaciones empresariales móviles</a>
      <span class="sep" style="left:681px"></span>
      <a href="#" style="left:743px">Metodología</a>
    </nav>
  </header>

  <div class="banner" role="img" aria-label="Blue chalkboard with the words Business Intelligence and related business terms written in chalk"></div>

  <main class="content">
    <h1>Business Intelligence</h1>
    <div class="photo" role="img" aria-label="Consultant thinking in front of a laptop"></div>
    <div class="intro">
      <h2>Our experience in business intelligence projects.</h2>
      <p>Lorem ipsum dolor sit amet, consectetur adipisicing elit, sed do eiusmod tempor incididunt ut labore et dolore magna aliqua. Ut enim ad minim veniam, quis nostrud exercitation ullamco laboris nisi ut aliquip ex commodo consequat. Duis aute irure dolor in reprehenderit in voluptate velit esse cillum dolore eu fugiat nulla pariatur. Excepteur sint occaecat cupidatat non proident, sunt in culpa qui officia deserunt mollit anim id est laborum. eu fugiat nulla pariatur. Excepteur sint occaecat cupidatat non proident, sunt in culpa qui officia deserunt mollit anim id est laborum.</p>
    </div>
    <div class="body">
      <p>Lorem ipsum dolor sit amet, consectetur adipisicing elit, sed do eiusmod tempor incididunt ut labore et dolore magna aliqua. Ut enim ad minim veniam, quis nostrud exercitation ullamco laboris nisi ut aliquip ex commodo consequat. Duis aute irure dolor in reprehenderit in voluptate velit esse cillum dolore eu fugiat nulla pariatur. Excepteur sint occaecat cupidatat non proident, sunt in culpa qui officia deserunt mollit anim id est laborum.eu fugiat nulla pariatur. Excepteur sint occaecat cupidatat non proident, sunt in culpa qui officia deserunt mollit anim id est laborum.eu fugiat nulla pariatur. Excepteur sint occaecat cupidatat non proident, sunt in culpa qui officia deserunt mollit anim id est laborum.eu fugiat nulla pariatur.</p>
      <p>Excepteur sint occaecat cupidatat non proident, sunt in culpa qui officia deserunt mollit anim id est laborum.eu fugiat nulla pariatur. Excepteur sint occaecat cupidatat non proident, sunt in culpa qui officia deserunt mollit anim id est laborum.eu fugiat nulla pariatur. Excepteur sint occaecat cupidatat non proident, sunt in culpa qui officia deserunt mollit anim id est laborum.eu fugiat nulla pariatur. Excepteur sint occaecat cupidatat non proident, sunt in culpa qui officia deserunt mollit anim id est laborum. eu fugiat nulla pariatur. Excepteur sint occaecat cupidatat non proident, sunt in culpa qui officia deserunt mollit anim id est laborum.</p>
      <h2>KRV Stockvault</h2>
      <p>Lorem ipsum dolor sit amet, consectetur adipisicing elit, sed do eiusmod tempor incididunt ut labore et dolore magna aliqua. Ut enim ad minim veniam, quis nostrud exercitation ullamco laboris nisi ut aliquip ex commodo consequat. Duis aute irure dolor in reprehenderit in voluptate velit esse cillum dolore eu fugiat nulla pariatur. Excepteur sint occaecat cupidatat non proident, sunt in culpa qui officia deserunt mollit anim id est laborum.</p>
    </div>
  </main>

  <footer class="footer">
    <div class="footer-inner">
      <h3>BUSINESS <em>INTELLIGENCE</em></h3>
      <p>Quisque gravida felis eu massa consectetur at malesuada nibh porttitor. Nam nunc nulla, tempus at viverra sit amet, semper nec diam. Phasellus tellus elit, placerat sit amet convallis at, bibendum vitae nisi.</p>
      <p>Phasellus vulputate consequat felis nec sagittis. Sed eget lectus in elit pretium euismod feugiat quis felis. Fusce ornare nulla at quam commodo non venenatis odio blandit. Donec sit amet nunc justo. Fusce ullamcorper, lacus sed lacinia fringilla, massa urna vulputate ante, vitae pharetra enim nibh nec diam.</p>
    </div>
  </footer>

  <div class="legal">© 2012, Lumivane , All Rights Reserved</div>
  <div class="social social--bottom"><span class="label">Follow Us</span><i></i><i></i><i></i><i></i></div>
</body>
</html>
```